Small boutique multi-family apartment developer needs premium website design.

We are a growing real estate development company specializing in multi family apartment development. Our company Mireval Stone Development focuses on passive real estate investors looking to maximize their current real estate portfolio by allowing us to develop and reposition their current properties allowing them more cashflow while we are also able to take over the management of their asset in order to ensure optimal performance on a consistent basis.

```html
<!DOCTYPE html>
<html lang="en">
<head>
<meta charset="UTF-8">
<title>Mireval Stone Development</title>
<link href="https://fonts.googleapis.com/css2?family=Prata&family=Inter:wght@400;600&family=Montserrat:wght@700&display=swap" rel="stylesheet">
<style>
  :root {
    --ink: #111418;
    --brand-blue: #1f5a8a;
    --accent: #d2542a;
    --band: #2f4a5c;
    --rule: #ececec;
    --white: #ffffff;
  }
  * { margin: 0; padding: 0; box-sizing: border-box; }
  html, body { width: 1200px; height: 3000px; overflow: hidden; background: var(--white); }
  body { position: relative; font-family: "Inter", Arial, sans-serif; color: var(--ink); }
  .serif { font-family: "Prata", Georgia, serif; font-weight: 400; }
  .abs { position: absolute; }

  /* Hero */
  .hero { position: absolute; left: 0; top: 0; width: 1200px; height: 687px; }
  .hero-photo {
    position: absolute; inset: 0 0 12px 0;
    background:
      linear-gradient(90deg, rgba(255,255,255,0.97) 0%, rgba(255,255,255,0.8) 18%, rgba(255,255,255,0) 50%),
      radial-gradient(ellipse at 40% 35%, #f1ede7 0%, #e4ddd3 25%, transparent 45%),
      radial-gradient(ellipse at 85% 20%, #8a6a55 0%, transparent 30%),
      linear-gradient(160deg, #5f6f7c 0%, #c9a582 40%, #d3a877 65%, #c18c5a 100%);
  }
  .hero-band { position: absolute; left: 0; bottom: 0; width: 1200px; height: 12px; background: var(--band); }

  .brand { display: flex; align-items: center; gap: 12px; }
  .brand-mark { width: 58px; height: 58px; border-radius: 50%; background: var(--brand-blue); flex: none; }
  .brand-name { font-family: "Prata", Georgia, serif; color: var(--brand-blue); font-size: 30px; line-height: 1.05; }

  .nav {
    position: absolute; left: 553px; top: 68px; width: 615px; height: 53px;
    background: var(--white); display: flex; align-items: center;
    font-family: "Prata", Georgia, serif; font-size: 26px; color: var(--ink);
  }
  .nav a { position: absolute; color: inherit; text-decoration: none; }

  .hero-title { left: 68px; top: 292px; font-size: 42px; line-height: 60px; width: 560px; }
  .hero-role { left: 74px; top: 463px; font-size: 22px; letter-spacing: 0.2px; }
  .btn {
    position: absolute; background: var(--accent); color: var(--white);
    border-radius: 30px; display: flex; align-items: center; justify-content: center;
    font-weight: 600; text-transform: uppercase; text-decoration: none;
  }
  .btn-call { left: 75px; top: 523px; width: 200px; height: 40px; font-size: 18px; }

  /* About */
  .about-title { left: 68px; top: 800px; font-size: 58px; }
  .about-copy { left: 68px; top: 912px; width: 430px; font-size: 22px; line-height: 29px; }
  .btn-inquire { left: 68px; top: 1061px; width: 236px; height: 48px; font-size: 21px; }
  .about-photo {
    left: 524px; top: 775px; width: 608px; height: 473px; border-radius: 26px;
    background: linear-gradient(120deg, #f4e7b5 0%, #b8a98c 25%, #3c4656 50%, #7b6d5d 72%, #c38c5a 100%);
  }
  .divider { left: 0; top: 1310px; width: 1200px; height: 1px; background: var(--rule); }

  /* Testimonials */
  .clients-title { left: 0; top: 1380px; width: 1187px; text-align: center; font-size: 56px; }
  .client { position: absolute; top: 1522px; width: 300px; text-align: center; }
  .client-photo { width: 140px; height: 140px; margin: 0 auto; border-radius: 4px; }
  .client-name { margin-top: 45px; font-size: 26px; font-weight: 600; }
  .client-quote { margin: 10px auto 0; width: 280px; font-size: 15px; line-height: 19.5px; }
  .stars { margin: 14px auto 0; display: block; }

  /* Contact */
  .contact-brand { left: 68px; top: 2075px; }
  .contact-title { left: 68px; top: 2203px; font-size: 58px; }
  .info-label { font-family: "Montserrat", Arial, sans-serif; font-weight: 700; font-size: 14px; letter-spacing: 0.3px; text-transform: uppercase; }
  .info-text { font-size: 15px; line-height: 19px; margin-top: 9px; }
  .contact-photo {
    left: 481px; top: 1986px; width: 719px; height: 672px;
    background: linear-gradient(135deg, #7a4a34 0%, #c98d6a 30%, #e9ddd3 55%, #a8613f 80%, #5e3a2c 100%);
  }
</style>
</head>
<body>

<header class="hero">
  <div class="hero-photo" role="img" aria-label="Hands presenting a row of small white model houses on a wooden desk"></div>
  <div class="hero-band"></div>

  <div class="brand abs" style="left:75px; top:48px;">
    <span class="brand-mark"></span>
    <span class="brand-name">Mireval Stone<br>Development</span>
  </div>

  <nav class="nav">
    <a href="#" style="left:24px;">Home</a>
    <a href="#" style="left:140px;">About Us</a>
    <a href="#" style="left:285px;">Testimonial</a>
    <a href="#" style="left:487px;">Contact</a>
  </nav>

  <h1 class="abs serif hero-title">Small boutique multi-family apartment developer</h1>
  <p class="abs hero-role">REAL ESTATE AGENT</p>
  <a href="#" class="btn btn-call">Call Us</a>
</header>

<section>
  <h2 class="abs serif about-title">Get to Know Me</h2>
  <p class="abs about-copy">With over a decade of experience in the real estate industry, I've got what it takes to find you your dream home. Nothing's impossible with me!</p>
  <a href="#" class="btn btn-inquire">Inquire Now</a>
  <div class="abs about-photo" role="img" aria-label="Developers in suits beside a desk with a cardboard model house and charts"></div>
  <div class="abs divider"></div>
</section>

<section>
  <h2 class="abs serif clients-title">Satisfied Clients</h2>

  <div class="client" style="left:98px;">
    <div class="client-photo" role="img" aria-label="Portrait of client Nadia Brennock" style="background:linear-gradient(160deg,#e6e2dc,#c9b8a6);"></div>
    <div class="client-name">Nadia Brennock</div>
    <p class="client-quote">Testimonials are short quotes from people who love your brand. It's a great way to convince customers to try your services.</p>
    <svg class="stars" width="134" height="24" viewBox="0 0 134 24"><g fill="#d2542a"><path id="st" d="M12 1l3.2 7 7.6.7-5.8 5 1.8 7.4L12 17.2 5.2 21.1 7 13.7 1.2 8.7 8.8 8z"/><use href="#st" x="27.5"/><use href="#st" x="55"/><use href="#st" x="82.5"/><use href="#st" x="110"/></g></svg>
  </div>

  <div class="client" style="left:451px;">
    <div class="client-photo" role="img" aria-label="Family photo of client Colin Ashwell" style="background:linear-gradient(160deg,#e3dcd2,#b89a80);"></div>
    <div class="client-name">Colin Ashwell</div>
    <p class="client-quote">Testimonials are short quotes from people who love your brand. It's a great way to convince customers to try your services.</p>
    <svg class="stars" width="134" height="24" viewBox="0 0 134 24"><g fill="#d2542a"><use href="#st"/><use href="#st" x="27.5"/><use href="#st" x="55"/><use href="#st" x="82.5"/><use href="#st" x="110"/></g></svg>
  </div>

  <div class="client" style="left:801px;">
    <div class="client-photo" role="img" aria-label="Family photo of client Marcus Delacroy" style="background:linear-gradient(160deg,#d9d4cc,#8a5a3e);"></div>
    <div class="client-name">Marcus Delacroy</div>
    <p class="client-quote">Testimonials are short quotes from people who love your brand. It's a great way to convince customers to try your services.</p>
    <svg class="stars" width="134" height="24" viewBox="0 0 134 24"><g fill="#d2542a"><use href="#st"/><use href="#st" x="27.5"/><use href="#st" x="55"/><use href="#st" x="82.5"/><use href="#st" x="110"/></g></svg>
  </div>
</section>

<footer>
  <div class="brand abs contact-brand">
    <span class="brand-mark"></span>
    <span class="brand-name">Mireval Stone<br>Development</span>
  </div>
  <h2 class="abs serif contact-title">Get in Touch</h2>

  <div class="abs" style="left:68px; top:2303px;">
    <div class="info-label">Mailing Address</div>
    <p class="info-text">48 Larkfield Row, Ashby Vale,<br>State, Country 20417</p>
  </div>
  <div class="abs" style="left:68px; top:2416px;">
    <div class="info-label">Email Address</div>
    <p class="info-text">hello@mirevalstone.com</p>
  </div>
  <div class="abs" style="left:68px; top:2509px;">
    <div class="info-label">Phone Number</div>
    <p class="info-text">(555) 310 4826</p>
  </div>

  <div class="abs contact-photo" role="img" aria-label="Hands passing a small model house with a red roof across a desk with documents"></div>
</footer>

</body>
</html>
```